Wine labels Velmora Wine Council - Nueva etiqueta El Consejo Regulador de vinos de Albarrán

Velmora Wines Council, based in southern Spain, are looking to create a new suite of wine labels which retain the elegance of the Sherry Wines industry while reinvigorating their image to the modern era and a new generation of Sherry Wine lovers. These labels will be used across the Velmora Wines Council's range of wines for the promotion of the Sherry Wines industry.

Your design must present at least two styles of Sherry Wines which demonstrate an elegant, modern interpretation and understanding of the unique mood and personality for these wines and the essence of southern Spain.

10 labels will be created based on the winning design, one for each of the unique varieties of Sherry Wines within the collection. This collection comprises of several different wine varieties including: Fino, Manzanilla, Amontillado, Oloroso, Palo Cortado, Medium, Cream, Pale Cream, Pedro Ximenez and Moscatel.

We recommend you visit our website www.velmora-vinos.example/wines as the source to understanding the origins and unique personality of these diverse wines.

El Consejo Regulador de los Vinos de Albarrán y Tordesal quiere renovar las etiquetas de los vinos utilizados para sus actividades de promoción genérica. Esta colección de vinos comprende las tipologías más importantes de la región que incluye: fino, manzanilla, amontillado, oloroso, palo cortado, pale cream, medium, cream, pedro ximénez y moscatel. Por lo tanto se precisan 10 etiquetas, una para cada uno de los vinos mencionados.
Updates

Project Deadline Extended
Reason: Due to some confusion with the deadline we wish to officially extend the deadline to allow designers one last week to submit their entries.

Target Market(s)

Industry, journalists, media, sommeliers, chefs, wine writers

Industry/Entity Type

Council

Requirements
Must have
• Front and Back label plus capsule:
• Front label can have either of the two official logos of the Velmora Wine council titled Vinos de Albarrán Digital or not, this is optional. Must include: Vino selecionado por el Consejo Regulador de la Denominacion de Origen, Name of the variety of wine eg FINO, percentage of alcohol eg 15% and quantity 75 cl.
• The back of the label must include the council logo titled Sellora and 4 additional logos positioned smaller. The Europa logo must appear larger than the 3 other logos. Space for descriptive text about the wine is also required.
• The dimensions of the bottle can be found at this link http://www.vidrialto.example/es/catalogo/vinos-y-espumosos/bordelesas/bd-orla
• Altura:305 mm
• Diámetro base:76,20 mm
• Diámetro hombro:82 mm
• Tipo boca:Cetie
• Peso:750 gr
• Capacidad:75 cl
• Etiqueta delantera y trasera y capsula
• La etiqueta delantera puede incluir el logo oficial del Consejo Regulador o el logo digital, o ninguno, esto es opcional. Debe incluir el siguiete texto: Vino selecionado por el Consejo Regulador de la Denominacion de Origen, el nombre de la variedad del vino, por ejemplo Fino, el porcentaje de alcohol, por ejemplo 15%, y la capacidad 75cl.
• La etiqueta trasera debe incluir el logo oficial Sellora del Consejo, y cuatro logos adicionales con una dimension menor. El Logo de ¨Europa invierte en las zonas rurales¨ debe ser de mayor tamaño que los otros. Se precisa espacio para el texto descriptivo de los vinos.
• Las dimensiones de la botella se puede encontrar en este enlace
• http://www.vidrialto.example/es/catalogo/vinos-y-espumosos/bordelesas/bd-orla
• Altura:305 mm
• Diámetro base:76,20 mm
• Diámetro hombro:82 mm
• Tipo boca:Cetie
• Peso:750 gr
• Capacidad:75 cl
Nice to have
• See our website velmora-vinos.example to understand the origin of the wines. Ver nuestra página web velmora-vinos.example para mejor entender los vinos.
Should not have
• Images of catavinos or stereotypical images from Spain such as flamenco dancers or guitars.

```html
<!DOCTYPE html>
<html lang="es">
<head>
<meta charset="utf-8">
<title>Amontillado – Etiqueta delantera</title>
<link href="https://fonts.googleapis.com/css2?family=Bodoni+Moda:wght@400;500&family=Roboto+Condensed:wght@300;400;500&display=swap" rel="stylesheet">
<style>
  :root {
    --backdrop: #e4e4e4;
    --paper: #ffffff;
    --ink: #2b2b2b;
    --ink-soft: #6a6a6a;
    --gold: #b19a3b;
    --horse-magenta: #c2207a;
    --horse-violet: #7b4fb4;
    --horse-blue: #2f8fd0;
    --horse-green: #2ea36a;
    --horse-lime: #b7d45a;
  }
  * { margin: 0; padding: 0; box-sizing: border-box; }
  html, body {
    width: 1200px; height: 1200px; overflow: hidden;
    background: var(--backdrop);
  }
  .front-label {
    position: absolute;
    left: 351px; top: 100px;
    width: 497px; height: 1000px;
    background: var(--paper);
    color: var(--ink);
    font-family: "Roboto Condensed", sans-serif;
  }
  .do-mark {
    position: absolute;
    top: 120px; left: 0; right: 0;
    display: flex; justify-content: center; align-items: center; gap: 10px;
    font-family: "Bodoni Moda", serif;
    font-size: 26px; letter-spacing: 6px;
    color: var(--ink);
  }
  .do-mark .square {
    width: 8px; height: 8px; background: var(--gold);
  }
  .horse-art {
    position: absolute;
    left: 50px; top: 249px;
    width: 403px; height: 412px;
    background: linear-gradient(135deg,
      var(--horse-magenta) 0%, var(--horse-violet) 22%,
      var(--horse-blue) 45%, var(--horse-green) 70%, var(--horse-lime) 100%);
    opacity: 0.85;
    clip-path: polygon(62% 0, 82% 6%, 80% 22%, 95% 45%, 80% 52%, 55% 60%, 40% 96%, 20% 92%, 0 80%, 10% 65%, 30% 55%, 45% 30%);
  }
  .variety-name {
    position: absolute;
    left: 0; right: 0; top: 686px;
    text-align: center;
    font-family: "Bodoni Moda", serif;
    font-weight: 400;
    font-size: 74px;
    letter-spacing: -1px;
    color: var(--ink);
  }
  .variety-name .initial { color: var(--gold); }
  .council-statement {
    position: absolute;
    left: 0; right: 0; top: 800px;
    text-align: center;
    line-height: 1.2;
  }
  .council-statement .lead,
  .council-statement .tail {
    font-weight: 300; font-size: 17px; color: var(--ink-soft);
  }
  .council-statement .council {
    font-weight: 500; font-size: 22px; color: var(--ink); margin: 2px 0;
  }
  .legal-line {
    position: absolute;
    left: 34px; right: 30px; top: 930px;
    display: flex; justify-content: space-between;
    font-weight: 300; font-size: 32px; color: var(--ink);
  }
</style>
</head>
<body>
  <div class="front-label">
    <div class="do-mark"><span class="square"></span>ALBARRÁN</div>

    <div class="horse-art" role="img" aria-label="Ilustración poligonal de un caballo encabritado en tonos magenta, azul y verde"></div>

    <h1 class="variety-name"><span class="initial">A</span>montillado</h1>

    <div class="council-statement">
      <p class="lead">Vino Seleccionado por el</p>
      <p class="council">CONSEJO REGULADOR</p>
      <p class="tail">de la Denominación de Origen</p>
    </div>

    <div class="legal-line">
      <span class="abv">15% Vol.</span>
      <span class="volume">75 cl.</span>
    </div>
  </div>
</body>
</html>
```